Varnel Supply requires a new business card.

We are an online professional tool store.

Target Market(s)

We target the professional technician.

Industry/Entity Type

Business

Contact Information for Business Card

VarnelSupply.com.au

sales@varnelsupply.example

Requirements
Must have
• Needs to look commercial and professional
Should not have
• No Australian Colors, maps or shapes.
• No Shapes of Tools

```html
<!DOCTYPE html>
<html lang="en">
<head>
<meta charset="utf-8">
<title>Varnel Supply – Business Card</title>
<link href="https://fonts.googleapis.com/css2?family=Source+Sans+3:wght@400;700&display=swap" rel="stylesheet">
<style>
  :root {
    --backdrop: #2a2a2a;
    --royal-blue: #0a22a8;
    --sky-blue: #0b8ab8;
    --accent-blue: #0c8fc4;
    --name-blue: #1e8fd8;
    --icon-blue: #4aa8e0;
    --paper: #f2f2f2;
    --white: #ffffff;
  }
  * { margin: 0; padding: 0; box-sizing: border-box; }
  html, body {
    width: 1200px; height: 960px; overflow: hidden;
    background: var(--backdrop);
    font-family: "Source Sans 3", sans-serif;
  }
  .canvas { position: relative; width: 1200px; height: 960px; }
  .card {
    position: absolute; width: 600px; height: 343px;
    border-radius: 18px; overflow: hidden;
  }
  .card-front { left: 314px; top: 113px; background: var(--royal-blue); }
  .card-back { left: 311px; top: 472px; background: var(--sky-blue); }
  .front-shape { position: absolute; inset: 0; }
  .contact-block { position: absolute; left: 34px; top: 62px; color: var(--white); }
  .person-name {
    font-weight: 700; font-size: 20px; color: var(--name-blue);
    letter-spacing: 0.3px; line-height: 22px;
  }
  .person-title { font-size: 15px; line-height: 18px; margin-top: 2px; }
  .address { margin-top: 30px; font-size: 15px; line-height: 19px; }
  .contact-list { list-style: none; margin-top: 8px; font-size: 15px; }
  .contact-list li { display: flex; align-items: center; height: 19.8px; }
  .contact-list svg { width: 14px; height: 14px; margin-right: 11px; fill: var(--icon-blue); }
  .front-brand {
    position: absolute; left: 320px; top: 148px; width: 260px; text-align: center;
    font-weight: 700; font-size: 34px; color: var(--royal-blue); letter-spacing: 0.5px;
  }
  .back-brand {
    position: absolute; left: 0; right: 0; top: 132px; text-align: center;
    font-weight: 700; font-size: 48px; color: var(--white); letter-spacing: 0.5px;
  }
  .back-website {
    position: absolute; left: 0; right: 0; top: 298px; text-align: center;
    font-size: 16px; color: var(--white); letter-spacing: 3.2px;
  }
</style>
</head>
<body>
<div class="canvas">
  <section class="card card-front">
    <svg class="front-shape" viewBox="0 0 600 343" aria-hidden="true">
      <path fill="var(--accent-blue)" d="M306,18 C236,110 250,262 396,343 L600,343 L600,0 Z"/>
      <path fill="var(--paper)" d="M314,0 C250,70 240,232 456,343 L600,343 L600,0 Z"/>
    </svg>
    <div class="contact-block">
      <div class="person-name">MARCUS HALE</div>
      <div class="person-title">PRESIDENT</div>
      <div class="address">4127 Ashcombe Road<br>Linden Vale, NY 11204</div>
      <ul class="contact-list">
        <li><svg viewBox="0 0 16 16"><path d="M1 6c0-2 3-3 7-3s7 1 7 3v1h-4V5.5H5V7H1zM3 8h10l1 6H2z"/></svg>555 0142 7781</li>
        <li><svg viewBox="0 0 16 16"><path d="M4 0h8v16H4zM5.5 2v10h5V2zM7 13.2h2v1.4H7z" fill-rule="evenodd"/></svg>555 0199 3460</li>
        <li><svg viewBox="0 0 16 16"><path d="M4 1h7v4H4zM1 6h14v6h-2v3H3v-3H1zM5 10v3h6v-3z" fill-rule="evenodd"/></svg>555 0173 2918</li>
        <li><svg viewBox="0 0 16 16"><path d="M1 3h14v10H1zM2 4l6 5 6-5z" fill-rule="evenodd"/></svg>sales@varnelsupply.example</li>
        <li><svg viewBox="0 0 16 16"><circle cx="8" cy="8" r="7"/><path fill="var(--royal-blue)" d="M5 4c2 0 3 1 2 3s-3 1-3 3M10 10c1-2 3-1 3-3"/></svg>VarnelSupply.com.au</li>
      </ul>
    </div>
    <div class="front-brand">Varnel Supply</div>
  </section>

  <section class="card card-back">
    <div class="back-brand">Varnel Supply</div>
    <div class="back-website">www.VarnelSupply.com.au</div>
  </section>
</div>
</body>
</html>
```